Educational outcome management software startup firm needs a graphic design

Our software startup firm, Pelvar Insight Technologies recently purchased a beautiful logo from Brushmarket (uploaded file). We are now looking for a graphic design to be used in the marketing activities of Pelvar Insight Technologies. See the uploaded picture of what a sketch of the graphic we are looking for.

```html
<!DOCTYPE html>
<html lang="en">
<head>
<meta charset="utf-8">
<title>Learner Journey Ecosystem — Pelvar Insight Technologies</title>
<link rel="stylesheet" href="https://fonts.googleapis.com/css2?family=Questrial&display=swap">
<style>
  :root {
    --navy: #2c3e6b;
    --red: #b5413a;
    --ring: #6f7d92;
    --zone-outer: #eceef2;
    --zone-middle: #dfe1e6;
    --zone-inner: #c5ccd8;
    --figure: #c9d2e3;
    --figure-deep: #9eabc4;
    --white: #ffffff;
  }
  * { box-sizing: border-box; margin: 0; padding: 0; }
  html, body { width: 1200px; height: 1200px; overflow: hidden; background: var(--white); }
  body { font-family: "Questrial", sans-serif; color: var(--navy); }
  .canvas { position: relative; width: 1200px; height: 1200px; }
  .rings { position: absolute; inset: 0; }

  .brand {
    position: absolute; left: 30px; top: 34px;
    display: flex; align-items: center; gap: 12px;
    font-size: 26px; color: var(--navy); letter-spacing: 0.5px;
  }
  .brand-mark { width: 22px; height: 22px; background: var(--red); }

  .node { position: absolute; transform: translate(-50%, -50%); text-align: center; line-height: 1.1; white-space: nowrap; }

  .stakeholder-label {
    background: var(--white); border: 4px solid var(--red); border-radius: 10px;
    font-size: 19.5px; padding: 5px 9px; letter-spacing: 0.6px;
  }
  .stakeholder-badge {
    width: 120px; height: 120px; border-radius: 50%;
    background: var(--white); border: 5px solid var(--red);
    display: flex; align-items: center; justify-content: center;
  }
  .stakeholder-art { width: 74px; height: 74px; border-radius: 12px; background: var(--figure); }

  .milestone {
    background: var(--white); border: 5px solid var(--navy); border-radius: 12px;
    font-size: 19px; padding: 7px 12px; letter-spacing: 0.4px;
  }
  .skill {
    background: var(--white); border: 5px solid var(--navy); border-radius: 12px;
    font-size: 18px; padding: 7px 10px; letter-spacing: 0.4px; line-height: 1.2;
  }
  .learner-figure {
    width: 124px; height: 150px; border-radius: 10px;
    background: linear-gradient(180deg, var(--figure) 0%, var(--figure-deep) 100%);
  }
  .learner-label {
    background: var(--white); border: 5px solid var(--red); border-radius: 8px;
    font-size: 25px; letter-spacing: 4px; padding: 8px 14px; line-height: 1.05;
    width: 146px;
  }
</style>
</head>
<body>
<div class="canvas">
  <svg class="rings" width="1200" height="1200" viewBox="0 0 1200 1200" aria-hidden="true">
    <defs>
      <circle id="dot-outer" cx="1075" cy="601" r="7" fill="#b5413a"/>
      <circle id="dot-middle" cx="917" cy="601" r="7" fill="#2c3e6b"/>
      <circle id="dot-inner" cx="779" cy="601" r="7" fill="#2c3e6b"/>
    </defs>
    <circle cx="601" cy="601" r="474" fill="var(--zone-outer)" stroke="var(--ring)" stroke-width="5"/>
    <circle cx="601" cy="601" r="316" fill="var(--zone-middle)" stroke="var(--ring)" stroke-width="5"/>
    <circle cx="601" cy="601" r="178" fill="var(--zone-inner)" stroke="var(--ring)" stroke-width="5"/>

    <g class="outer-dots">
      <use href="#dot-outer" transform="rotate(-100 601 601)"/><use href="#dot-outer" transform="rotate(-80 601 601)"/>
      <use href="#dot-outer" transform="rotate(-55 601 601)"/><use href="#dot-outer" transform="rotate(-35 601 601)"/>
      <use href="#dot-outer" transform="rotate(-12 601 601)"/><use href="#dot-outer" transform="rotate(12 601 601)"/>
      <use href="#dot-outer" transform="rotate(35 601 601)"/><use href="#dot-outer" transform="rotate(55 601 601)"/>
      <use href="#dot-outer" transform="rotate(80 601 601)"/><use href="#dot-outer" transform="rotate(100 601 601)"/>
      <use href="#dot-outer" transform="rotate(125 601 601)"/><use href="#dot-outer" transform="rotate(145 601 601)"/>
      <use href="#dot-outer" transform="rotate(168 601 601)"/><use href="#dot-outer" transform="rotate(192 601 601)"/>
      <use href="#dot-outer" transform="rotate(-145 601 601)"/><use href="#dot-outer" transform="rotate(-125 601 601)"/>
    </g>
    <g class="middle-dots">
      <use href="#dot-middle" transform="rotate(-104 601 601)"/><use href="#dot-middle" transform="rotate(-76 601 601)"/>
      <use href="#dot-middle" transform="rotate(-43 601 601)"/><use href="#dot-middle" transform="rotate(-19 601 601)"/>
      <use href="#dot-middle" transform="rotate(14 601 601)"/><use href="#dot-middle" transform="rotate(42 601 601)"/>
      <use href="#dot-middle" transform="rotate(76 601 601)"/><use href="#dot-middle" transform="rotate(104 601 601)"/>
      <use href="#dot-middle" transform="rotate(137 601 601)"/><use href="#dot-middle" transform="rotate(166 601 601)"/>
      <use href="#dot-middle" transform="rotate(-162 601 601)"/><use href="#dot-middle" transform="rotate(-136 601 601)"/>
    </g>
    <g class="inner-dots">
      <use href="#dot-inner" transform="rotate(-118 601 601)"/><use href="#dot-inner" transform="rotate(-62 601 601)"/>
      <use href="#dot-inner" transform="rotate(-46 601 601)"/><use href="#dot-inner" transform="rotate(-6 601 601)"/>
      <use href="#dot-inner" transform="rotate(9 601 601)"/><use href="#dot-inner" transform="rotate(44 601 601)"/>
      <use href="#dot-inner" transform="rotate(62 601 601)"/><use href="#dot-inner" transform="rotate(118 601 601)"/>
      <use href="#dot-inner" transform="rotate(136 601 601)"/><use href="#dot-inner" transform="rotate(173 601 601)"/>
      <use href="#dot-inner" transform="rotate(-171 601 601)"/><use href="#dot-inner" transform="rotate(-134 601 601)"/>
    </g>
  </svg>

  <div class="brand"><span class="brand-mark"></span><span class="brand-name">Pelvar Insight Technologies</span></div>

  <!-- Stakeholders: outer ring -->
  <div class="node stakeholder-badge" style="left:604px;top:126px"><div class="stakeholder-art" role="img" aria-label="Icon of a parent with child"></div></div>
  <div class="node stakeholder-label" style="left:604px;top:51px">Parent/Guardian</div>

  <div class="node stakeholder-badge" style="left:941px;top:263px"><div class="stakeholder-art" role="img" aria-label="Icon of hands holding a résumé"></div></div>
  <div class="node stakeholder-label" style="left:941px;top:192px">Employer</div>

  <div class="node stakeholder-badge" style="left:1079px;top:601px"><div class="stakeholder-art" role="img" aria-label="Icon of a board with a graduation cap"></div></div>
  <div class="node stakeholder-label" style="left:1079px;top:517px">Post-secondary<br>education system</div>

  <div class="node stakeholder-badge" style="left:939px;top:939px"><div class="stakeholder-art" role="img" aria-label="Icon of an official at a podium"></div></div>
  <div class="node stakeholder-label" style="left:939px;top:867px">Government</div>

  <div class="node stakeholder-badge" style="left:604px;top:1077px"><div class="stakeholder-art" role="img" aria-label="Icon of a laptop with a shopping cart"></div></div>
  <div class="node stakeholder-label" style="left:604px;top:1006px">Interaction marketplace</div>

  <div class="node stakeholder-badge" style="left:268px;top:938px"><div class="stakeholder-art" role="img" aria-label="Icon of a school administrator"></div></div>
  <div class="node stakeholder-label" style="left:268px;top:867px">School administrator</div>

  <div class="node stakeholder-badge" style="left:128px;top:600px"><div class="stakeholder-art" role="img" aria-label="Icon of a group of counselors"></div></div>
  <div class="node stakeholder-label" style="left:128px;top:527px">School conselor</div>

  <div class="node stakeholder-badge" style="left:268px;top:263px"><div class="stakeholder-art" role="img" aria-label="Icon of a teacher pointing at a board"></div></div>
  <div class="node stakeholder-label" style="left:268px;top:191px">Teacher</div>

  <!-- Milestones: middle ring -->
  <div class="node milestone" style="left:604px;top:270px">High School<br>Graduation</div>
  <div class="node milestone" style="left:882px;top:434px">Employment</div>
  <div class="node milestone" style="left:891px;top:753px">Admission into<br>Post-secondary<br>Institution</div>
  <div class="node milestone" style="left:602px;top:916px">Competion<br>of elementary<br>school</div>
  <div class="node milestone" style="left:323px;top:754px">Graduation<br>from higher<br>education</div>
  <div class="node milestone" style="left:321px;top:434px">Enterpreneu</div>

  <!-- Skills: inner ring -->
  <div class="node skill" style="left:602px;top:408px">reading<br>skills</div>
  <div class="node skill" style="left:761px;top:512px">writing<br>skills</div>
  <div class="node skill" style="left:765px;top:681px">study<br>skills</div>
  <div class="node skill" style="left:602px;top:787px">information<br>technology<br>skills</div>
  <div class="node skill" style="left:436px;top:681px">social<br>skills</div>
  <div class="node skill" style="left:441px;top:512px">STEM<br>skills</div>

  <!-- Centre: learner -->
  <div class="node learner-figure" style="left:602px;top:550px" role="img" aria-label="Illustration of a graduating student in cap and gown"></div>
  <div class="node learner-label" style="left:602px;top:669px">learner/<br>student</div>
</div>
</body>
</html>
```